A new company focused on starting and investing in transformative businesses.

We need a simple and clean website with a few pages. we like larkmeadow.com as a starting point. we want the landing page to be very simple with an option to click through on the top right into INVESTOR LOGIN. then we want to be able to scroll down to see more about our company.

Target Market(s)

professional

Coding

Coded - Design and coding required

Number of Pages Required

2 page

Font styles to use
Serif
Sans Serif

Requirements
Must have
• HALVERN BUILDERS logo (attached as a file) on the top with INVESTOR LOGIN as a click through on the right. Please model the click through from larkmeadow.com. The description (also written in attached file) should be on the landing page. we do not want to have to scroll to read the description.

Then we can scroll down to read more about Halvern including the mission and the two types of businesses. More is detailed on the attached file called "Halvern Website Syntax"
Should not have
• should not be slow loading with lots of fancy graphics. should not be busy and with too many colors.

```html
<!DOCTYPE html>
<html lang="en">
<head>
<meta charset="utf-8">
<title>Halvern Builders</title>
<link href="https://fonts.googleapis.com/css2?family=Montserrat:wght@400;500;600;700&display=swap" rel="stylesheet">
<style>
  :root {
    --ink-dark: #282828;
    --brand-blue: #0a5aa0;
    --text-body: #2a2a2a;
    --white: #ffffff;
  }
  * { margin: 0; padding: 0; box-sizing: border-box; }
  html, body { width: 1200px; height: 749px; overflow: hidden; }
  body { font-family: 'Montserrat', sans-serif; background: var(--white); position: relative; }

  .hero { position: absolute; left: 0; top: 0; width: 1200px; height: 313px; background: var(--ink-dark); }
  .brand { position: absolute; display: flex; align-items: center; gap: 6px; color: var(--white); }
  .brand-mark { width: 22px; height: 31px; background: var(--brand-blue); }
  .brand-name { font-weight: 600; font-size: 11.5px; line-height: 13px; letter-spacing: 0.3px; }
  .hero .brand { left: 225px; top: 16px; }

  .investor-login {
    position: absolute; left: 849px; top: 16px; width: 125px; height: 30px;
    background: var(--brand-blue); color: var(--white); text-decoration: none;
    font-size: 11.5px; font-weight: 400; display: flex; align-items: center; justify-content: center;
  }

  .tagline {
    position: absolute; left: 225px; top: 110px; width: 560px;
    border-left: 1.5px solid var(--brand-blue); padding-left: 13px;
    color: var(--white); font-size: 24.5px; font-weight: 400; line-height: 34px;
    margin-top: -6px; padding-top: 0;
  }
  .scroll-cue { position: absolute; left: 587px; top: 267px; }

  .about { position: absolute; left: 0; top: 313px; width: 1200px; height: 305px; }
  .mission {
    position: absolute; left: 225px; top: 30px; width: 340px;
    color: var(--brand-blue); font-size: 19.5px; font-weight: 400; line-height: 26.3px;
  }
  .focus { position: absolute; left: 599px; width: 380px; }
  .focus h2 { font-size: 19.5px; font-weight: 600; color: var(--text-body); letter-spacing: 0.2px; line-height: 24px; }
  .focus p { margin-top: 8px; margin-left: 1px; font-size: 11.3px; line-height: 17px; color: var(--text-body); }
  .focus.ground-up { top: 32px; }
  .focus.special { top: 164px; }

  .footer { position: absolute; left: 0; top: 618px; width: 1200px; height: 131px; background: var(--brand-blue); }
  .footer .brand { left: 225px; top: 37px; }
  .footer .brand-mark { background: var(--white); }
  .media-contact { position: absolute; left: 224px; top: 85px; color: var(--white); font-size: 11.5px; font-weight: 500; }
</style>
</head>
<body>
  <header class="hero">
    <div class="brand">
      <span class="brand-mark"></span>
      <span class="brand-name">HALVERN<br>BUILDERS</span>
    </div>
    <a class="investor-login" href="#">Investor Login</a>
    <p class="tagline">Halvern Builders is an entrepreneurial firm focused on building and growing transformational companies.</p>
    <svg class="scroll-cue" width="26" height="31" viewBox="0 0 26 31" aria-hidden="true">
      <path d="M13 1 V29 M1 17 L13 29 L25 17" fill="none" stroke="#0a5aa0" stroke-width="1"/>
    </svg>
  </header>

  <main class="about">
    <p class="mission">Our mission is to build meaningful businesses that create enduring value by impacting people in a measurable way.</p>
    <section class="focus ground-up">
      <h2>GROUND UP</h2>
      <p>Our ground up business applies a proven analytic process to identify value edge, a form of competitive advantage. We architect transformational companies and are deliberate in creating the foundation necessary to lead an industry.</p>
    </section>
    <section class="focus special">
      <h2>SPECIAL OPPORTUNITIES</h2>
      <p>We partner with exceptional teams that create value by transforming lives. Our investment focus includes large companies and spin-outs</p>
    </section>
  </main>

  <footer class="footer">
    <div class="brand">
      <span class="brand-mark"></span>
      <span class="brand-name">HALVERN<br>BUILDERS</span>
    </div>
    <p class="media-contact">For media inquiries, please contact press@halvernbuilders.com</p>
  </footer>
</body>
</html>
```